Software allocation system needs a business card design

We need a business card designed for our software platform - www.tolvexa.com.au

At the moment the logo and website is all black and white, we are happy for suggestions on implementing some colour throughout either the logo or business card.

Industry/Entity Type

Software

Font styles to use
Sans Serif

Colors

Designer to choose colors to be used in the design.

```html
<!DOCTYPE html>
<html lang="en">
<head>
<meta charset="utf-8">
<title>Tolvexa Business Card</title>
<link rel="stylesheet" href="https://fonts.googleapis.com/css2?family=Open+Sans:wght@300;400;700;800&display=swap">
<style>
  :root {
    --page-bg: #e9e9ea;
    --card-bg: #ffffff;
    --panel-dark: #3a3a3c;
    --panel-band: rgba(255,255,255,0.22);
    --ink-dark: #2b2b2b;
    --ink-mid: #6a6a6a;
    --accent-blue: #3aa0dc;
    --stripe-black: #1e1e1e;
  }
  * { margin: 0; padding: 0; box-sizing: border-box; }
  html, body { width: 1200px; height: 900px; overflow: hidden; }
  body {
    background: var(--page-bg);
    font-family: "Open Sans", Arial, sans-serif;
    position: relative;
  }
  .business-card {
    position: absolute;
    left: 100px; top: 160px;
    width: 1000px; height: 580px;
    background: var(--card-bg);
    box-shadow: 0 18px 40px rgba(0,0,0,0.18);
    overflow: hidden;
  }
  .card-graphics { position: absolute; inset: 0; }
  .web-address {
    position: absolute;
    left: 24px; top: 160px;
    color: #ffffff;
    font-weight: 700;
    font-size: 24px;
    line-height: 34px;
    letter-spacing: 1px;
    white-space: nowrap;
  }
  .brand {
    position: absolute;
    left: 450px; top: 36px;
  }
  .brand-name {
    font-weight: 300;
    font-size: 80px;
    letter-spacing: 4px;
    color: var(--ink-dark);
    line-height: 1;
  }
  .brand-tagline {
    margin-top: 8px;
    font-weight: 700;
    font-size: 18px;
    color: var(--ink-dark);
    letter-spacing: 0.5px;
    white-space: nowrap;
  }
  .person {
    position: absolute;
    right: 60px; top: 200px;
    text-align: right;
    line-height: 1.3;
  }
  .person-name {
    font-weight: 800;
    font-size: 38px;
    color: var(--accent-blue);
    letter-spacing: 1px;
  }
  .person-role {
    font-weight: 400;
    font-size: 24px;
    color: var(--ink-dark);
    letter-spacing: 1px;
  }
  .contact {
    position: absolute;
    left: 460px; top: 310px;
    color: var(--ink-mid);
    font-weight: 700;
    font-size: 24px;
    line-height: 1.35;
    letter-spacing: 0.5px;
    white-space: nowrap;
  }
  .contact-heading {
    color: var(--ink-dark);
    font-size: 32px;
    line-height: 1.3;
    font-weight: 700;
    text-decoration: underline;
    text-underline-offset: 6px;
    margin-bottom: 6px;
  }
  .contact-line span { display: inline-block; width: 125px; }
  .address {
    position: absolute;
    left: 60px; top: 462px;
    color: var(--ink-mid);
    font-weight: 700;
    font-size: 22px;
    line-height: 1.3;
    letter-spacing: 0.5px;
    white-space: nowrap;
  }
</style>
</head>
<body>
  <div class="business-card">
    <svg class="card-graphics" width="1000" height="580" viewBox="0 0 1000 580" aria-hidden="true">
      <defs>
        <clipPath id="panel-shape">
          <polygon points="0,0 300,0 430,230 0,380"/>
        </clipPath>
      </defs>
      <polygon points="0,0 300,0 430,230 0,380" fill="var(--panel-dark)"/>
      <rect x="0" y="152" width="440" height="50" fill="var(--panel-band)" clip-path="url(#panel-shape)"/>
      <rect x="0" y="538" width="1000" height="4" fill="var(--stripe-black)"/>
      <rect x="0" y="546" width="1000" height="8" fill="var(--accent-blue)"/>
      <rect x="0" y="558" width="1000" height="4" fill="var(--stripe-black)"/>
      <rect x="0" y="566" width="1000" height="3" fill="var(--stripe-black)"/>
    </svg>

    <div class="web-address">WWW.TOLVEXA.COM.AU</div>

    <div class="brand">
      <div class="brand-name">TOLVEXA</div>
      <div class="brand-tagline">PLANNING &amp; COMPLIANCE FOR HEAVY INDUSTRY</div>
    </div>

    <div class="person">
      <div class="person-name">ROWAN ELLERY</div>
      <div class="person-role">GRAPHIC DESIGNER</div>
    </div>

    <div class="contact">
      <div class="contact-heading">CONTACT US</div>
      <div class="contact-line"><span>PHONE :</span>00 123 444 566</div>
      <div class="contact-line"><span>TEL NO :</span>00 444 666 678</div>
      <div class="contact-line">WWW.INFO@DOMAIN.COM</div>
    </div>

    <div class="address">
      <div>24 STREET, YOUR HOUSE, CITY 4220</div>
      <div>UNITED KINGDOM</div>
    </div>
  </div>
</body>
</html>
```